A3 Menus for new international restaurant in Singapore.

Looking for new A3 menu design for indoor & outdoor (beautiful garden and trees) restaurant that caters for expat and local families. International menu, cool jazz vibe, great for couples and families. Restaurant called Brass Cove Parlour. I have attached some of the logos we use. Will consider black and white or color options. Restaurant located on a hill where there were tin mines many years ago, hence the name and branding. Looking for three menus (1) Dinner (2) Lunch (3) weekend brunch.

Target Market(s)

Families, young couples and professionals.

Industry/Entity Type

Restaurant

Font styles to use
Serif
Sans Serif

Requirements
Must have
• All food layout on one side of A3, one for each attached menu. Also a space for drinks list on the back.
Nice to have
• Use some of the logo material we have attached.
Should not have

```html
<!DOCTYPE html>
<html lang="en">
<head>
<meta charset="utf-8">
<title>Brass Cove Parlour — Dinner Menu</title>
<link href="https://fonts.googleapis.com/css2?family=Roboto+Condensed:wght@700&family=Crimson+Text:ital,wght@0,400;1,400&display=swap" rel="stylesheet">
<style>
  :root {
    --ink: #111111;
    --paper: #ffffff;
    --rule: #1a1a1a;
  }
  * { margin: 0; padding: 0; box-sizing: border-box; }
  html, body { width: 848px; height: 1200px; overflow: hidden; background: var(--paper); }
  .menu {
    position: relative;
    width: 848px;
    height: 1200px;
    background: var(--paper);
    color: var(--ink);
    font-family: "Crimson Text", Georgia, serif;
  }
  .frame {
    position: absolute;
    left: 35px; top: 72px;
    width: 778px; height: 1082px;
    border: 2px solid var(--rule);
  }
  .brand {
    position: absolute;
    left: 364px; top: 34px;
    width: 120px;
    padding: 4px 0;
    background: var(--paper);
    text-align: center;
    font-family: "Roboto Condensed", "Arial Narrow", sans-serif;
    font-weight: 700;
    font-size: 21px;
    line-height: 22px;
    letter-spacing: 1px;
    text-transform: uppercase;
    color: var(--ink);
  }
  .section-head {
    position: absolute;
    display: flex;
    align-items: center;
    gap: 22px;
    font-family: "Roboto Condensed", "Arial Narrow", sans-serif;
    font-weight: 700;
    font-size: 17px;
    letter-spacing: 2.4px;
    text-transform: uppercase;
    height: 20px;
  }
  .section-head::before,
  .section-head::after {
    content: "";
    flex: 1;
    height: 1px;
    background: var(--rule);
  }
  .col {
    position: absolute;
    width: 196px;
  }
  .dish { margin-bottom: 12px; }
  .dish-name {
    font-family: "Roboto Condensed", "Arial Narrow", sans-serif;
    font-weight: 700;
    font-size: 8.8px;
    line-height: 11.5px;
  }
  .dish-desc {
    font-size: 9.6px;
    line-height: 11.5px;
  }
  .dish-desc em { font-style: italic; }
  .footnote {
    position: absolute;
    left: 35px; top: 1133px;
    width: 778px;
    text-align: center;
    font-style: italic;
    font-size: 8.8px;
  }
</style>
</head>
<body>
<main class="menu">
  <div class="frame"></div>
  <div class="brand">Brass<br>Cove<br>Parlour</div>

  <h2 class="section-head" style="left:108px;top:140px;width:411px;">Starters</h2>
  <h2 class="section-head" style="left:538px;top:140px;width:195px;">Platters</h2>

  <section class="col" style="left:108px;top:182px;">
    <div class="dish"><p class="dish-name">Roasted Red Capsicum Soup | $9.50</p><p class="dish-desc">with popped rice and coconut cream</p></div>
    <div class="dish"><p class="dish-name">Beetroot Salad | $9.50</p><p class="dish-desc">slow-cooked beetroot, assorted onions, creamy goat's cheese, walnuts</p></div>
    <div class="dish"><p class="dish-name">Beef Tartare | $22</p><p class="dish-desc">hand-chopped sirloin and tenderloin mixed with capers, pickles &amp; shallots, served with bone marrow and crostini</p></div>
  </section>
  <section class="col" style="left:323px;top:182px;">
    <div class="dish"><p class="dish-name">Classic Greek Salad | $16.50</p><p class="dish-desc">cherry tomatoes, feta, kalamata olives, green capsicum &amp; cucumber</p></div>
    <div class="dish"><p class="dish-name">Crab Salad | $17.50</p><p class="dish-desc">blue swimmer crab remoulade, tiger prawns, frisse salad leaves and homemade brioche melba toast</p></div>
    <div class="dish"><p class="dish-name">Duck Croquettes | $16.50</p><p class="dish-desc">crispy panko-coated duck rillettes, accompanied by parsnip mash, garlic confit and sweet wine sauce</p></div>
  </section>
  <section class="col" style="left:538px;top:182px;">
    <div class="dish"><p class="dish-name">Seafood Platter | $38 or $70</p><p class="dish-desc">selection of gravlax, smoked fish, marinated seafood, pumpernickel bread and dipping sauces. $38 for 2 to share or $70 for 4 to share</p></div>
    <div class="dish"><p class="dish-name">Charcuterie Platter | $32 or $60</p><p class="dish-desc">3 types of charcuterie, duck rillettes, pickles, crostini and wholegrain mustard. $32 for 2 to share or $60 for 4 to share</p></div>
  </section>

  <h2 class="section-head" style="left:108px;top:366px;width:625px;">Main Courses</h2>
  <section class="col" style="left:108px;top:411px;">
    <div class="dish"><p class="dish-name">Brass Cove Parlour Burger | $22</p><p class="dish-desc">200gms ground prime beef served in a homemade brioche bun with lettuce, tomato and mayo, served with a side of fries. Top it with cheese or bacon, or both -- add $2 each</p></div>
    <div class="dish"><p class="dish-name">Brass Cove Parlour Bangers &amp; Mash | $22</p><p class="dish-desc">prime pork sausages, buttery mashed potato covered in onion &amp; cider gravy</p></div>
    <div class="dish"><p class="dish-name">Hay Smoked Pork Ribs | $26</p><p class="dish-desc">home-smoked, slow-cooked ribs, served with spicy chimichurri sauce and fries</p></div>
    <div class="dish"><p class="dish-name">Pan Seared Black Cod | $35</p><p class="dish-desc">served on a bed of vermicelli, lemongrass, fresh chilli and kaffir lime leaves</p></div>
  </section>
  <section class="col" style="left:323px;top:411px;">
    <div class="dish"><p class="dish-name">Beef Tenderloin | $35</p><p class="dish-desc">200gms grilled to your choice, served with roasted vine tomatoes and red wine gravy, accompanied by buttery mashed potato or fries</p></div>
    <div class="dish"><p class="dish-name">Brass Cove Parlour's Seafood Stew | $30</p><p class="dish-desc">classic seafood stew, served in the pan with fresh black cod, prawns, calamari, clams and mussels, cooked in a prawn bisque, with bread for dipping</p></div>
    <div class="dish"><p class="dish-name">Roast Chicken | $38</p><p class="dish-desc">share a whole bird for 2, with jus and your choice of two sides. <em>Please allow 25 minutes to prepare</em></p></div>
    <div class="dish"><p class="dish-name">Roast Pork Belly | $85</p><p class="dish-desc">served with apple compote and your choice of two sides. Whole belly shared among 3-4 people. <em>Please allow 45 minutes to roast</em></p></div>
  </section>
  <section class="col" style="left:538px;top:411px;">
    <div class="dish"><p class="dish-name">Beef T-Bone | $75</p><p class="dish-desc">600gms T-Bone grilled, served with red wine gravy and your choice of two sides. Shared among 2 people. <em>Please allow 25 minutes to cook</em></p></div>
    <div class="dish"><p class="dish-name">Strigoli | $22</p><p class="dish-desc">with beef ragu bolognese</p></div>
    <div class="dish"><p class="dish-name">Linguini | $23</p><p class="dish-desc">with a light creamy carbonara sauce, with smoked pancetta</p></div>
    <div class="dish"><p class="dish-name">Rigatoni | $20</p><p class="dish-desc">with aglio, olio and pepperoncino. Add prawns for $5</p></div>
    <div class="dish"><p class="dish-name">Risotto | $22</p><p class="dish-desc">with rich porcini mushrooms and crutin cheese</p></div>
  </section>

  <h2 class="section-head" style="left:108px;top:666px;width:197px;">Sides</h2>
  <h2 class="section-head" style="left:323px;top:664px;width:410px;">Pizza</h2>
  <section class="col" style="left:108px;top:702px;">
    <div class="dish"><p class="dish-name">Coconut Corn on the Cob | $9</p></div>
    <div class="dish"><p class="dish-name">Onion Mashed Potato | $9</p></div>
    <div class="dish"><p class="dish-name">Peas and Smoked Pancetta | $9</p></div>
    <div class="dish"><p class="dish-name">Green Beans with Toasted Pine<br>Nuts and Garlic Confit | $9</p></div>
    <div class="dish"><p class="dish-name">Mixed Salad | $9</p></div>
    <div class="dish"><p class="dish-name">Truffle Fries | $9</p></div>
    <div class="dish"><p class="dish-name">French Fries | $7</p></div>
    <div class="dish"><p class="dish-name">Bread Rolls | $4</p><p class="dish-desc">with olive oil and balsamic vinegar</p></div>
  </section>
  <section class="col" style="left:323px;top:702px;">
    <div class="dish"><p class="dish-name">Margherita | $24</p><p class="dish-desc">roast tomato, mozzarella and fresh basil</p></div>
    <div class="dish"><p class="dish-name">Bloody Margherita | $28</p><p class="dish-desc">a take on the classic aperitif: vodka flushed roast tomatoes, mozzarella, celery salt, worcester and chilli sauces</p></div>
    <div class="dish"><p class="dish-name">Spinach &amp; Ricotta | $25</p><p class="dish-desc">home-smoked, slow-cooked ribs, served with spicy chimichurri sauce and fries</p></div>
    <div class="dish"><p class="dish-name">Pan Seared Black Cod | $35</p><p class="dish-desc">with toasted pine nuts, cherry tomatoes and ricotta cheese</p></div>
  </section>
  <section class="col" style="left:538px;top:702px;">
    <div class="dish"><p class="dish-name">Umami Chicken | $27</p><p class="dish-desc">with baby king oyster mushrooms, shaved parmesan and fresh thyme</p></div>
    <div class="dish"><p class="dish-name">Parma Ham | $29</p><p class="dish-desc">with semi-dried tomato and fresh arugula leaves</p></div>
    <div class="dish"><p class="dish-name">Hay-smoked Pulled Pork &amp;<br>Pancetta | $29</p><p class="dish-desc">home-smoked, slow cooked pulled pork rib, with sausage, pancetta and onion</p></div>
    <div class="dish"><p class="dish-name">Smoked Pancetta | $29</p><p class="dish-desc">with shitake mushrooms, spring onions, chilli and brie</p></div>
    <div class="dish"><p class="dish-name">Seafood | $30</p><p class="dish-desc">with smoked salmon, prawns, calamari, onions, and crushed roasted tomato.</p></div>
  </section>

  <h2 class="section-head" style="left:108px;top:959px;width:625px;">Desserts</h2>
  <section class="col" style="left:108px;top:1003px;">
    <div class="dish"><p class="dish-name">Frozen Mojito | $14</p><p class="dish-desc">lime and rum sorbet with spearmint granita, soda foam and sugar crumbs</p></div>
    <div class="dish"><p class="dish-name">Chocolate Cake | $15</p><p class="dish-desc">with raspberry coulis, vanilla ice cream and almond brittle</p></div>
  </section>
  <section class="col" style="left:323px;top:1003px;">
    <div class="dish"><p class="dish-name">Mango Chilli Pie | $15</p><p class="dish-desc">with rice pudding ice cream and coconut sago</p></div>
    <div class="dish"><p class="dish-name">Gianduja Chocolate Fondant | $15</p><p class="dish-desc">with orange coulis and latte cremoso</p></div>
    <div class="dish"><p class="dish-name">Ice Cream | $5 per scoop</p></div>
  </section>
  <section class="col" style="left:538px;top:1003px;">
    <div class="dish"><p class="dish-name">Hay-infused Panna Cotta | $10</p><p class="dish-desc">with spiced honey sauce and apple butter</p></div>
    <div class="dish"><p class="dish-name">Cheese Board | $23</p><p class="dish-desc">selection of three worldwide cheeses, grapes, crostini and chutney</p></div>
  </section>

  <p class="footnote">All prices are in Singapore Dollars and are subject to GST &amp; 10% Service Charge</p>
</main>
</body>
</html>
```